Redesign a Start-Up Dating Website

Website: https://morvelink.com.
Make sure the design has an island style theme.
I would like the 7 pages of my website to have a new and professional look. I want the same colors to remain, but I want a creative look for all the pages. This is a dating website that is in the startup stage. So, I want to give my entire website a custom makeover. I want something that will stand out from the other dating sites. Something that will attract more people to want to use my services, and hopefully get new members.
Target Market(s)
Dating
Industry/Entity Type
Dating
Coding
Coded - Design and coding required
Number of Pages Required
5+ page
Font styles to use
Other font styles liked:
- Decorative, San Serif
Requirements
Must have
- The design must have the original colors and a stylish font to go along. The design must be creative, welcoming, and professional. I would like an island style theme for the website. This is a dating website so make sure that the design is tailored to that aspect.
Nice to have
- It would be nice to have a decorative font and a professional style on all the pages. Make sure the design will be mobile responsive and friendly for all the pages on the website.
Should not have
- The design should not be bland and uncreative.

```html
<!DOCTYPE html>
<html lang="en">
<head>
<meta charset="utf-8">
<title>Morvelink – Dating is Easy</title>
<link rel="stylesheet" href="https://fonts.googleapis.com/css2?family=Mulish:wght@400;600;700&family=Playfair+Display:wght@700;800&family=Rozha+One&display=swap">
<style>
:root{
  --ink:#333333;
  --text:#555555;
  --muted:#777777;
  --orange:#f18a1c;
  --teal:#2db39b;
  --purple:#6b4399;
  --purple-light:#9a78c2;
  --band:#e9e9e9;
  --white:#ffffff;
  --line:#cfcfcf;
}
*{box-sizing:border-box;margin:0;padding:0}
html,body{width:1200px;height:2564px;overflow:hidden}
body{font-family:"Mulish",Arial,sans-serif;color:var(--text);background:var(--white);position:relative}
.abs{position:absolute}
.serif{font-family:"Rozha One","Playfair Display",serif;font-weight:400}

/* top bar */
.topbar{position:absolute;left:0;top:0;width:1200px;height:41px;background:var(--ink)}
.social{position:absolute;left:74px;top:12px;display:flex;gap:16px}
.social span{width:17px;height:17px;border-radius:50%;background:#cfcfcf;display:block}
.login{position:absolute;right:126px;top:10px;color:#eee;font-size:19px}
.menu{position:absolute;right:76px;top:12px;width:24px}
.menu i{display:block;height:2px;background:#eee;margin-bottom:6px}

/* header */
.header{position:absolute;left:0;top:41px;width:1200px;height:106px;background:var(--white);box-shadow:0 3px 8px rgba(0,0,0,.18);z-index:2}
.brand{position:absolute;left:80px;top:25px;display:flex;align-items:center;gap:12px}
.brand-dot{width:56px;height:56px;border-radius:50%;background:var(--teal)}
.brand-name{font-family:"Mulish",sans-serif;font-weight:700;font-size:44px;color:var(--teal);letter-spacing:.5px}
.nav{position:absolute;right:77px;top:40px;display:flex;gap:26px;font-size:19px;color:#555}

/* hero */
.hero{position:absolute;left:0;top:147px;width:1200px;height:583px;
  background:linear-gradient(90deg,#eef4f8 0%,#e4edf3 38%,#c9dbe3 55%,#7f9aa5 70%,#2f7d86 85%,#3a8f9a 100%)}
.hero-title{position:absolute;left:77px;top:232px;font-family:"Playfair Display",serif;font-weight:700;font-size:41px;line-height:46px;color:#2b2b2b}
.hero-sub{position:absolute;left:77px;top:333px;width:570px;font-size:21px;line-height:29px;color:#333}
.ribbon{position:absolute;left:0;top:147px;z-index:3}

/* welcome */
.welcome{position:absolute;left:0;top:730px;width:1200px;height:290px;text-align:center}
.welcome h4{position:absolute;top:40px;width:100%;font-family:"Playfair Display",serif;font-size:21px;color:#222}
.welcome h2{position:absolute;top:68px;width:100%;font-size:37px;color:var(--orange)}
.welcome p{position:absolute;top:112px;left:180px;width:840px;font-size:15.5px;line-height:25px;color:#666}
.btn{display:inline-block;background:var(--teal);color:#fff;font-size:19px;letter-spacing:.3px;text-align:center}
.welcome .btn{position:absolute;left:511px;top:200px;width:176px;height:39px;line-height:39px}

/* members */
.members{position:absolute;left:0;top:1020px;width:1200px;height:395px;background:var(--band);text-align:center}
.members h2{position:absolute;top:36px;width:100%;font-size:36px;color:var(--orange)}
.members .lead{position:absolute;top:81px;width:100%;font-size:20px;color:#555}
.member{position:absolute;top:117px;width:220px;text-align:center}
.member .photo{width:166px;height:166px;border-radius:50%;margin:0 auto;border:3px solid #fff}
.member h3{margin-top:24px;font-family:"Playfair Display",serif;font-size:21px;color:#555}
.member p{margin-top:5px;font-size:16px;color:#666}

/* quick search */
.search{position:absolute;left:0;top:1415px;width:1200px;height:376px;border-top:2px solid var(--purple);border-bottom:2px solid var(--purple)}
.search-panel{position:absolute;left:0;top:-2px;width:579px;height:378px;background:var(--purple)}
.field label{position:absolute;color:#fff;font-size:15px}
.select{position:absolute;border:1.5px solid #fff;color:#fff;font-size:15px;padding-left:9px;display:flex;align-items:center}
.select svg{position:absolute;right:10px;top:50%;margin-top:-5px}
.notch{position:absolute;left:559px;top:182px;width:0;height:0;border-top:20px solid transparent;border-bottom:20px solid transparent;border-right:20px solid #fff}
.search-copy{position:absolute;left:649px;top:110px}
.search-copy h2{font-size:37px;color:var(--orange)}
.search-copy p{font-size:15.5px;color:#555;line-height:33px}

/* benefits */
.benefits{position:absolute;left:0;top:1791px;width:1200px;height:658px;text-align:center}
.benefits h2{position:absolute;top:40px;width:100%;font-size:37px;color:var(--orange)}
.benefits .b1{position:absolute;top:91px;width:100%;font-size:15.5px;color:#555}
.benefits .b2{position:absolute;top:115px;width:100%;font-size:15.5px;color:#555}
.benefits .btn{position:absolute;left:460px;top:150px;width:280px;height:41px;line-height:41px}
.divider{position:absolute;left:77px;top:238px;width:1046px;height:1px;background:var(--line)}
.divider span{position:absolute;left:50%;top:-14px;transform:translateX(-50%);background:#fff;padding:0 20px;font-family:"Playfair Display",serif;font-size:20px;color:#444}
.step{position:absolute;top:290px;width:330px;text-align:center}
.step svg{display:block;margin:0 auto}
.step h3{margin-top:10px;font-family:"Playfair Display",serif;font-size:22px;color:var(--orange)}
.step p{margin:8px auto 0;width:320px;font-size:15.5px;line-height:25px;color:#555}

/* footer */
.footer{position:absolute;left:0;top:2449px;width:1200px;height:115px;background:var(--ink);text-align:center}
.footer-nav{position:absolute;top:23px;width:100%;display:flex;justify-content:center;gap:35px;font-size:16px;color:#eee}
.footer-rule{position:absolute;left:223px;top:61px;width:760px;height:1px;background:#666}
.copyright{position:absolute;top:78px;width:100%;font-size:16px;color:#ddd}
</style>
</head>
<body>

<div class="topbar">
  <div class="social"><span></span><span></span><span></span></div>
  <div class="login">Login</div>
  <div class="menu"><i></i><i></i><i></i></div>
</div>

<header class="header">
  <div class="brand"><span class="brand-dot"></span><span class="brand-name">Morvelink</span></div>
  <nav class="nav"><span>Home</span><span>About</span><span>Search</span><span>Members</span><span>Extras</span><span>Premium</span><span>Contact</span></nav>
</header>

<section class="hero" role="img" aria-label="Smiling couple embracing outdoors in bright daylight">
</section>
<svg class="ribbon" width="1200" height="70" viewBox="0 0 1200 70">
  <path d="M100 0 H1140 Q780 20 660 30 L600 60 L540 30 Q420 20 100 0 Z" fill="#6b4399" opacity="0.9"/>
  <text x="600" y="33" text-anchor="middle" font-family="Mulish, sans-serif" font-size="18" fill="#fff">REGISTER NOW</text>
  <path d="M591 43 L609 43 L600 51 Z" fill="#fff"/>
</svg>
<div class="hero-title abs" style="top:379px">Dating is EASY with<br>Morvelink</div>
<p class="hero-sub" style="top:480px">Sigh-up For Free 30 Days Free Trial Enjoy All The Benefits Morvelink has to Offer With a Full Membership.</p>

<section class="welcome">
  <h4>Welcome!</h4>
  <h2 class="serif">Know About Morvelink</h2>
  <p>Morvelink aims to provide a straight-forward, easy-to-use online dating service. I won't over-complicate things or reduce the amount of people you can talk to with algorithms. I know that sometimes, opposites attract and sparks can fly with the last person you thought you'd be interested in-so I won't hide anybody from you.</p>
  <span class="btn">KNOW MORE</span>
</section>

<section class="members">
  <h2 class="serif">Join this Community of 1 Morvelink Members</h2>
  <div class="lead">new added profile</div>
  <div class="member" style="left:59px"><div class="photo" role="img" aria-label="Member profile photo" style="background:radial-gradient(circle at 40% 40%,#f3d9c4,#c99a6e 70%,#8a6a4b)"></div><h3>Member Name</h3><p>Age:21 , New York</p></div>
  <div class="member" style="left:275px"><div class="photo" role="img" aria-label="Member profile photo" style="background:radial-gradient(circle at 50% 45%,#f1d5c3,#c7a08b 60%,#f2f2f2)"></div><h3>Member Name</h3><p>Age:21 , New York</p></div>
  <div class="member" style="left:490px"><div class="photo" role="img" aria-label="Member profile photo" style="background:radial-gradient(circle at 50% 50%,#e9c09a,#7a2a22 60%,#2a1412)"></div><h3>Member Name</h3><p>Age:21 , New York</p></div>
  <div class="member" style="left:705px"><div class="photo" role="img" aria-label="Member profile photo" style="background:radial-gradient(circle at 50% 50%,#d9a88a,#8a5a42 60%,#3a2a22)"></div><h3>Member Name</h3><p>Age:21 , New York</p></div>
  <div class="member" style="left:919px"><div class="photo" role="img" aria-label="Member profile photo" style="background:radial-gradient(circle at 50% 45%,#5a3a2a,#3a2a3a 55%,#1a1420)"></div><h3>Member Name</h3><p>Age:21 , New York</p></div>
</section>

<section class="search">
  <div class="search-panel">
    <div class="field">
      <label style="left:79px;top:76px">i'm a</label>
      <div class="select" style="left:79px;top:92px;width:207px;height:41px">Man<svg width="12" height="8" viewBox="0 0 12 8"><path d="M1 1 L6 6 L11 1" stroke="#fff" stroke-width="2" fill="none"/></svg></div>
      <label style="left:310px;top:76px">Seeking a</label>
      <div class="select" style="left:308px;top:92px;width:206px;height:41px">Women<svg width="12" height="8" viewBox="0 0 12 8"><path d="M1 1 L6 6 L11 1" stroke="#fff" stroke-width="2" fill="none"/></svg></div>
      <label style="left:79px;top:160px">Age</label>
      <div class="select" style="left:79px;top:176px;width:207px;height:41px">18<svg width="12" height="8" viewBox="0 0 12 8"><path d="M1 1 L6 6 L11 1" stroke="#fff" stroke-width="2" fill="none"/></svg></div>
      <label style="left:310px;top:160px">To</label>
      <div class="select" style="left:308px;top:176px;width:206px;height:41px">99<svg width="12" height="8" viewBox="0 0 12 8"><path d="M1 1 L6 6 L11 1" stroke="#fff" stroke-width="2" fill="none"/></svg></div>
      <label style="left:79px;top:244px">Country</label>
      <div class="select" style="left:79px;top:260px;width:435px;height:40px">Afghanistan<svg width="12" height="8" viewBox="0 0 12 8"><path d="M1 1 L6 6 L11 1" stroke="#fff" stroke-width="2" fill="none"/></svg></div>
    </div>
    <div class="notch"></div>
  </div>
  <div class="search-copy">
    <h2 class="serif">Quick search</h2>
    <p>Let's find your perfect match today</p>
    <p>Find your perfect Match for Free!</p>
    <p>Online dating made easy on morvelink.com</p>
  </div>
</section>

<section class="benefits">
  <h2 class="serif">Benefits</h2>
  <div class="b1">Affordable</div>
  <div class="b2">Easy Sign-Up and Cancellation Process</div>
  <span class="btn">VIEW MEMBERSHIP PLANS</span>
  <div class="divider"><span>online</span></div>

  <div class="step" style="left:71px">
    <svg width="200" height="190" viewBox="0 0 200 190">
      <ellipse cx="78" cy="168" rx="64" ry="10" fill="#555" opacity=".55"/>
      <circle cx="100" cy="88" r="80" fill="#7d56ad"/>
      <circle cx="100" cy="88" r="66" fill="#fff"/>
      <circle cx="95" cy="70" r="15" fill="#555"/>
      <path d="M65 122 Q65 92 95 92 Q125 92 125 122 Z" fill="#555"/>
      <circle cx="122" cy="116" r="11" fill="#555" stroke="#fff" stroke-width="2"/>
      <path d="M117 121 L127 111" stroke="#fff" stroke-width="2"/>
    </svg>
    <h3>Create a Profile</h3>
    <p>Let people know all about you; the good and the quirky-show the world your true colors and find someone with the same unique qualities as you.</p>
  </div>

  <div class="step" style="left:431px">
    <svg width="200" height="190" viewBox="0 0 200 190">
      <ellipse cx="78" cy="168" rx="64" ry="10" fill="#555" opacity=".55"/>
      <circle cx="100" cy="88" r="80" fill="#7d56ad"/>
      <circle cx="100" cy="88" r="66" fill="#fff"/>
      <circle cx="95" cy="68" r="16" fill="#555"/>
      <path d="M64 124 Q64 90 95 90 Q126 90 126 124 Z" fill="#555"/>
      <circle cx="122" cy="116" r="12" fill="#555" stroke="#fff" stroke-width="2"/>
      <path d="M122 123 L116 116 Q114 111 118 110 Q121 110 122 113 Q123 110 126 110 Q130 111 128 116 Z" fill="#fff"/>
    </svg>
    <h3>Find Matches</h3>
    <p>Browse other users and feel the excitement of getting your first message and getting to know potential dates in a safe and fun environment.</p>
  </div>

  <div class="step" style="left:797px">
    <svg width="200" height="190" viewBox="0 0 200 190">
      <ellipse cx="78" cy="168" rx="64" ry="10" fill="#555" opacity=".55"/>
      <circle cx="100" cy="88" r="80" fill="#7d56ad"/>
      <circle cx="100" cy="88" r="66" fill="#fff"/>
      <path d="M100 132 L68 98 Q58 84 70 72 Q84 62 100 78 Q116 62 130 72 Q142 84 132 98 Z" fill="none" stroke="#555" stroke-width="3"/>
      <path d="M100 132 L68 98 Q58 84 70 72 Q84 62 100 78 Z" fill="#555"/>
    </svg>
    <h3>Start Dating</h3>
    <p>Once you've found your potential soulmate, it's time to meet up and say 'Hello' to the start of your journey together</p>
  </div>
</section>

<footer class="footer">
  <nav class="footer-nav"><span>Home</span><span>About</span><span>Search</span><span>Members</span><span>Extras</span><span>Premium</span><span>Contact</span><span>Login</span><span>Register</span></nav>
  <div class="footer-rule"></div>
  <div class="copyright">2017 ©Morvelink. - All Rights Reserved.</div>
</footer>

</body>
</html>
```